Business Cards used to invite people to our church

We are a church and have need of a business card sized advertisement that allows our members to hand them out in order to invite people to the church. I need the front of the card to say "You're Invited" or "Come Check us out". with the service times on the back of the card later.
I have attached one of the OLD cards we have used in the past, but we want a complete makeover, into a more modern style that does not require the image.
I am also replacing the old logo with a newer "flat" logo which is attached.
Please use marketing colors. (blue or red or something that catches attention)
Create a card that DOES NOT have the picture of the two people on the front
The information on the sample card back is correct to go onto new card
Target Market(s)
anyone
Industry/Entity Type
Business
Contact Information for Business Card
sertice times and address information which you can get from the sample card I uploaded. It should have "You're Invited" or "Come Check us out" on the front of the card with out logo.
Look and feel
Each slider illustrates characteristics of the customer's brand and the style your logo design should communicate.

```html
<!DOCTYPE html>
<html lang="en">
<head>
<meta charset="utf-8">
<title>Grace Harbor Ministries – Invitation Card</title>
<link rel="stylesheet" href="https://fonts.googleapis.com/css2?family=Pinyon+Script&family=Source+Sans+3:wght@400;600;700&display=swap">
<style>
  :root {
    --backdrop: #2e2623;
    --card-blue: #478bcb;
    --ink: #0d0d0d;
    --card-shadow: rgba(0, 0, 0, 0.55);
  }
  * { box-sizing: border-box; margin: 0; padding: 0; }
  html, body {
    width: 1200px;
    height: 844px;
    overflow: hidden;
    background: var(--backdrop);
  }
  .canvas {
    width: 1200px;
    height: 844px;
    display: flex;
    align-items: center;
    justify-content: center;
    gap: 60px;
  }
  .card {
    width: 500px;
    height: 286px;
    background: var(--card-blue);
    color: var(--ink);
    box-shadow: 0 14px 30px var(--card-shadow);
    position: relative;
  }

  /* Front */
  .card-front {
    display: flex;
    align-items: center;
    justify-content: center;
  }
  .invite-line {
    font-family: "Pinyon Script", cursive;
    font-size: 72px;
    line-height: 0.95;
    text-align: center;
    font-weight: 400;
  }
  .invite-line span { display: block; }

  /* Back */
  .card-back {
    font-family: "Source Sans 3", sans-serif;
    padding: 26px 70px 0 70px;
    display: flex;
    flex-direction: column;
    align-items: center;
  }
  .ministry-name {
    display: flex;
    align-items: center;
    gap: 10px;
    font-family: "Source Sans 3", sans-serif;
    font-weight: 600;
    font-size: 24px;
    letter-spacing: 1.5px;
    text-transform: uppercase;
  }
  .ministry-dot {
    width: 22px;
    height: 22px;
    border-radius: 50%;
    background: var(--ink);
  }
  .contact {
    margin-top: 18px;
    text-align: center;
    font-weight: 700;
    font-size: 15px;
    line-height: 1.35;
  }
  .schedule {
    list-style: none;
    width: 100%;
    margin-top: 22px;
    font-size: 14px;
    font-weight: 400;
  }
  .schedule li {
    display: flex;
    align-items: baseline;
    margin-bottom: 8px;
  }
  .schedule .leader {
    flex: 1;
    border-bottom: 1.5px dotted var(--ink);
    margin: 0 3px;
    transform: translateY(-3px);
  }
</style>
</head>
<body>
  <main class="canvas">
    <section class="card card-front" aria-label="Card front">
      <h1 class="invite-line"><span>Come Check us</span><span>out</span></h1>
    </section>

    <section class="card card-back" aria-label="Card back">
      <div class="ministry-name"><span class="ministry-dot"></span>Grace Harbor Ministries</div>
      <p class="contact">2480 Cedar Lane - Maple, Tx 75000<br>1-800-555-0142</p>
      <ul class="schedule">
        <li><span class="day">Sunday</span><span class="leader"></span><span class="time">9:00 Am</span></li>
        <li><span class="day">Sunday</span><span class="leader"></span><span class="time">11:00 Am</span></li>
        <li><span class="day">Wed. Bible Class</span><span class="leader"></span><span class="time">7:00 Pm</span></li>
      </ul>
    </section>
  </main>
</body>
</html>
```